Holloway Photography.
I really don't know what should go here
Simple
Glen Holloway
Owner
4820 NE Corvel Dr Ankeny Ia 50023
holloway.photography@brevanmail.com
hollowayphotography.net
I am thinking that i will put a photo, or just my logo on one side, and the rest of the info on the other.
This is one of those moments...
let us tell your story.

```html
<!DOCTYPE html>
<html lang="en">
<head>
<meta charset="utf-8">
<title>Holloway Photography – Business Cards</title>
<link href="https://fonts.googleapis.com/css2?family=Cinzel:wght@500&family=Open+Sans:wght@400;700&family=Tinos&display=swap" rel="stylesheet">
<style>
  :root{
    --page:#ece9e4;
    --card-white:#ffffff;
    --card-black:#111111;
    --stripe-grey:#9a9a9a;
    --ink:#1a1a1a;
    --ink-soft:#555555;
    --on-dark:#f2f2f2;
  }
  html,body{margin:0;padding:0;width:1200px;height:852px;overflow:hidden;background:var(--page);}
  .canvas{position:relative;width:1200px;height:852px;}
  .card{position:absolute;width:540px;height:310px;border-radius:22px;overflow:hidden;background:var(--card-white);box-shadow:0 6px 18px rgba(0,0,0,.18);}
  .card--front{left:40px;top:271px;}
  .card--back{left:620px;top:271px;}
  .card__shape{position:absolute;inset:0;}
  .brand{position:absolute;display:flex;align-items:center;gap:12px;}
  .brand__mark{width:46px;height:46px;border-radius:50%;background:var(--ink);flex:none;}
  .brand__name{font-family:"Cinzel",serif;font-weight:500;font-size:18px;color:var(--ink);white-space:nowrap;}
  .person{position:absolute;text-align:center;}
  .person__name{font-family:"Open Sans",sans-serif;font-weight:700;font-size:15px;color:var(--ink);}
  .person__role{font-family:"Open Sans",sans-serif;font-size:11px;color:var(--ink-soft);margin-top:1px;}
  .contact{position:absolute;right:28px;text-align:right;font-family:"Tinos",serif;color:var(--on-dark);font-size:13px;line-height:1.35;}
  .contact__row{display:flex;justify-content:flex-end;align-items:center;gap:8px;}
  .icon{width:12px;height:12px;flex:none;}
  .web{position:absolute;right:28px;bottom:18px;text-align:right;font-family:"Tinos",serif;color:var(--on-dark);font-size:13px;line-height:1.55;}
  /* front card */
  .card--front .brand{left:40px;top:44px;}
  .card--front .person{left:150px;top:118px;}
  .card--front .contact{top:124px;}
  /* back card */
  .card--back .brand{left:40px;top:92px;flex-direction:column;gap:10px;}
  .card--back .brand__mark{width:56px;height:56px;}
  .card--back .brand__name{font-size:16px;}
  .card--back .person{right:52px;top:36px;}
  .card--back .contact{top:150px;}
</style>
</head>
<body>
<main class="canvas">

  <section class="card card--front" aria-label="Business card, front">
    <svg class="card__shape" viewBox="0 0 540 310" aria-hidden="true">
      <path d="M540,-6 C482,140 300,205 0,222 L0,310 L540,310 Z" fill="var(--stripe-grey)"/>
      <path d="M540,8 C492,152 312,220 0,236 L0,310 L540,310 Z" fill="var(--card-black)"/>
    </svg>
    <div class="brand">
      <span class="brand__mark"></span>
      <span class="brand__name">Holloway Photography.</span>
    </div>
    <div class="person">
      <div class="person__name">Glen Holloway</div>
      <div class="person__role">Owner</div>
    </div>
    <div class="contact">
      <div>4820 NE Corvel</div>
      <div>Dr Ankeny Ia 50023</div>
      <div class="contact__row">515-555-0142
        <svg class="icon" viewBox="0 0 12 12"><path d="M2.5 1 L4.5 1 L5.2 3.6 L4 4.6 C4.7 6 5.9 7.2 7.4 8 L8.4 6.8 L11 7.5 L11 9.5 C11 10.3 10.3 11 9.5 11 C5 11 1 7 1 2.5 C1 1.7 1.7 1 2.5 1 Z" fill="var(--on-dark)"/></svg>
      </div>
    </div>
    <div class="web">
      <div class="contact__row">holloway.photography@brevanmail.com <svg class="icon" viewBox="0 0 12 12"><circle cx="6" cy="6" r="5" fill="none" stroke="var(--on-dark)" stroke-width="1.4"/><circle cx="6" cy="6" r="2" fill="var(--on-dark)"/></svg></div>
      <div class="contact__row">www.hollowayphotography.net <svg class="icon" viewBox="0 0 12 12"><circle cx="6" cy="6" r="5" fill="none" stroke="var(--on-dark)" stroke-width="1.4"/><path d="M1 6 H11 M6 1 C3.5 4 3.5 8 6 11 M6 1 C8.5 4 8.5 8 6 11" fill="none" stroke="var(--on-dark)" stroke-width="1"/></svg></div>
    </div>
  </section>

  <section class="card card--back" aria-label="Business card, back">
    <svg class="card__shape" viewBox="0 0 540 310" aria-hidden="true">
      <path d="M540,-6 C410,70 290,250 20,310 L540,310 Z" fill="var(--stripe-grey)"/>
      <path d="M540,14 C428,88 312,264 60,310 L540,310 Z" fill="var(--card-black)"/>
    </svg>
    <div class="person">
      <div class="person__name">Glen Holloway</div>
      <div class="person__role">Owner</div>
    </div>
    <div class="brand">
      <span class="brand__mark"></span>
      <span class="brand__name">Holloway Photography.</span>
    </div>
    <div class="contact">
      <div>4820 NE Corvel</div>
      <div>Dr Ankeny Ia 50023</div>
      <div class="contact__row">515-555-0142
        <svg class="icon" viewBox="0 0 12 12"><path d="M2.5 1 L4.5 1 L5.2 3.6 L4 4.6 C4.7 6 5.9 7.2 7.4 8 L8.4 6.8 L11 7.5 L11 9.5 C11 10.3 10.3 11 9.5 11 C5 11 1 7 1 2.5 C1 1.7 1.7 1 2.5 1 Z" fill="var(--on-dark)"/></svg>
      </div>
    </div>
    <div class="web">
      <div class="contact__row">holloway.photography@brevanmail.com <svg class="icon" viewBox="0 0 12 12"><circle cx="6" cy="6" r="5" fill="none" stroke="var(--on-dark)" stroke-width="1.4"/><circle cx="6" cy="6" r="2" fill="var(--on-dark)"/></svg></div>
      <div class="contact__row">www.hollowayphotography.net <svg class="icon" viewBox="0 0 12 12"><circle cx="6" cy="6" r="5" fill="none" stroke="var(--on-dark)" stroke-width="1.4"/><path d="M1 6 H11 M6 1 C3.5 4 3.5 8 6 11 M6 1 C8.5 4 8.5 8 6 11" fill="none" stroke="var(--on-dark)" stroke-width="1"/></svg></div>
    </div>
  </section>

</main>
</body>
</html>
```